24Std Betreuung Flyer Senioren
Zielgruppe
Wir vermitteln Ihnen Pflegekräfte aus Polen in 24h Betreuung. Zu diesem Zweck arbeiten wir mit unseren Partnerunternehmen in Polen und Litauen, welche ihre Pflegekraft im Rahmen der EU Dienstleistungsfreiheit legal nach Deutschland vermitteln. Das von uns vermittelte Personal ist freundlich und gut ausgebildet und verfügt über ausreichende bis gute Deutschkenntnisse. Unsere Agentur übernimmt die Koordinierung und Klärung aller Angelegenheiten für die An- und Abreise ihrer Pflegekraft. Das Personal wohnt mit der pflegebürftigen Person zusammen, wodurch wir eine 24h Betreuung realisieren können.
Aufgabenstellung
Seniorengerecht und nicht zu modern, übersichtlich nicht zu klein geschrieben evtl mit lizenzfreien Bildern von Senioren
Format: 6 seitig Wickelfalz
Informationen auf ww.altershilfe-plus.de

```html
<!DOCTYPE html>
<html lang="de">
<head>
<meta charset="utf-8">
<title>24h Betreuung – Pflegekräfte aus Polen</title>
<link rel="stylesheet" href="https://fonts.googleapis.com/css2?family=Arimo:ital,wght@0,400;0,700;1,400;1,700&display=swap">
<style>
  :root {
    --brand-blue: #1f4f9e;
    --bullet-blue: #1d4e9b;
    --text-dark: #151515;
    --bg-light: #f4f4f4;
    --bg-mid: #d9d9d9;
    --photo-skin: #d9b8a4;
    --photo-white: #eef0f2;
    --photo-green: #8aa25a;
    --photo-blue: #3f6fa7;
    --photo-brown: #8a6a4e;
  }
  * { margin: 0; padding: 0; box-sizing: border-box; }
  html, body { width: 1131px; height: 1200px; overflow: hidden; }
  body {
    font-family: "Arimo", Arial, sans-serif;
    color: var(--text-dark);
    background: #ffffff;
  }
  .flyer-panel {
    position: relative;
    width: 1131px;
    height: 1200px;
    overflow: hidden;
    background: linear-gradient(115deg, var(--bg-light) 0%, #e6e6e6 35%, var(--bg-mid) 60%, #ececec 80%, #cfcfcf 100%);
  }
  .side-band {
    position: absolute; left: 0; top: 0;
    width: 42px; height: 1200px;
    background: var(--brand-blue);
  }
  .headline {
    position: absolute; left: 42px; top: 44px; width: 520px;
    text-align: center;
    line-height: 52px;
  }
  .headline .lead {
    display: block; font-weight: 700; font-size: 37px; letter-spacing: -0.3px;
  }
  .headline .sub {
    display: block; font-style: italic; font-size: 38px; margin-top: 8px;
  }
  .photo-top {
    position: absolute; left: 500px; top: 0; width: 631px; height: 318px;
    background:
      linear-gradient(90deg, rgba(235,235,235,1) 0%, rgba(235,235,235,0) 18%),
      radial-gradient(ellipse at 30% 45%, var(--photo-skin) 0%, transparent 30%),
      radial-gradient(ellipse at 80% 40%, #cfc3b8 0%, transparent 35%),
      linear-gradient(180deg, var(--photo-white) 0%, #dde3ea 70%, #5a8ec4 100%);
    box-shadow: 0 4px 6px rgba(0,0,0,0.25);
  }
  .photo-framed {
    position: absolute; left: 67px; top: 240px; width: 469px; height: 402px;
    border: 6px solid #ffffff;
    box-shadow: 2px 3px 8px rgba(0,0,0,0.35);
    background:
      radial-gradient(ellipse at 35% 40%, var(--photo-skin) 0%, transparent 22%),
      radial-gradient(ellipse at 28% 75%, var(--photo-blue) 0%, transparent 40%),
      radial-gradient(ellipse at 75% 55%, #3b8fc2 0%, transparent 35%),
      linear-gradient(180deg, var(--photo-green) 0%, #c2a86a 50%, #9b9b8a 100%);
  }
  .intro-text {
    position: absolute; left: 79px; top: 652px; width: 460px;
    font-style: italic; font-size: 20.5px; line-height: 24.5px;
  }
  .intro-text p { margin-bottom: 35px; }
  .intro-text p.wide-gap { margin-bottom: 58px; }
  .service-list {
    position: absolute; left: 566px; top: 342px; width: 520px;
    list-style: none;
    font-style: italic; font-size: 20.5px; line-height: 29px;
  }
  .service-list li { position: relative; padding-left: 22px; margin-bottom: 26px; }
  .service-list li::before {
    content: ""; position: absolute; left: 0; top: 10px;
    width: 9px; height: 9px; border-radius: 50%; background: var(--text-dark);
  }
  .service-list li.highlight { color: var(--bullet-blue); font-weight: 700; }
  .service-list li.highlight::before { background: var(--text-dark); }
  .service-list .narrow-gap { display: block; height: 29px; }
  .photo-seniors {
    position: absolute; left: 735px; top: 570px; width: 370px; height: 560px;
    background:
      radial-gradient(ellipse at 35% 30%, #7d5a48 0%, transparent 35%),
      radial-gradient(ellipse at 75% 35%, #c7b9a5 0%, transparent 32%),
      radial-gradient(ellipse at 50% 75%, #b9a58c 0%, transparent 45%),
      radial-gradient(ellipse at 50% 50%, rgba(138,106,78,0.35) 0%, transparent 70%);
    border-radius: 40% 40% 20% 20%;
  }
</style>
</head>
<body>
<main class="flyer-panel">
  <div class="side-band"></div>
  <div class="photo-top" role="img" aria-label="Foto: Pflegerin im weißen Kittel lächelt eine ältere Dame an"></div>

  <h1 class="headline">
    <span class="lead">Wir vermitteln Ihnen<br>Pflegekräfte aus Polen</span>
    <span class="sub">in 24h Betreuung.</span>
  </h1>

  <div class="photo-framed" role="img" aria-label="Foto: Pflegerin umarmt einen älteren Herrn im Rollstuhl im Garten"></div>

  <section class="intro-text">
    <p>Zu diesem Zweck arbeiten wir mit unseren<br>Partnerunternehmen in Polen, welche ihre<br>Pflegekraft im Rahmen der EU Dienstleistungs-<br>freiheit legal nach Deutschland vermitteln.</p>
    <p>Das von uns vermittelte Personal ist freundlich<br>und gut ausgebildet und verfügt über ausreich-<br>ende bis gute Deutschkenntnisse.</p>
    <p class="wide-gap">Unsere Agentur übernimmt die Koordinierung<br>und Klärung aller Angelegenheiten für die An-<br>und Abreise ihrer Pflegekraft.</p>
    <p>Das Personal wohnt mit der pflegebedürftigen<br>Person zusammen, wodurch wir eine 24h Betreu-<br>ung realisieren können.</p>
  </section>

  <div class="photo-seniors" role="img" aria-label="Foto: zwei fröhliche Senioren sitzen nebeneinander, einer hebt einen Gehstock, der andere hält einen Fußball"></div>

  <ul class="service-list">
    <li class="highlight">In einer eingehenden Beratung bei Ihnen zu<br>Hause erstellen wir eine detaillierte Anamnese<br>um so eine sorgfältige Auswahl des geeigneten<br>Pflegepersonals für Sie zu treffen.</li>
    <li>Gerne beraten wir Sie und führen eine Bedarfs-<br>analyse mit Ihnen persönlich durch, um so ge-<br>währleisten zu können, dass wir die richtige<br>Pflegekraft für Ihren<br>Bedarf finden.</li>
    <li>Diese Bedarfs-<br>analyse<br>wird<span class="narrow-gap"></span>durch einen<br>Fragebogen<br>sowie ein Analyse-<br>Gespräch mit Ihnen<br>ermittelt. Sollten<br>Sie mal Fragen<br>haben bezüglich<br>des betreunenden<br>Personals oder in<br>anderen Angelegen-<br>heiten stehen wir Ihnen<br>jederzeit als Ansprech-<br>partner zur Verfügung.</li>
  </ul>
</main>
</body>
</html>
```